Business Card Design

We have a current business card but would like to update it to make it look more modern.

Please see attached business card.

I would like the logo to be updated - make it more modern. Colors for logo and text can stay the same (Navy Blue and Black/Grey). Sorry I don't have a vector file for the logo.

Single sided business card but try to include all the details in the card attached.

No need to include logo/text for Larkmoor Containers and Drosval

I want the card to look less busy.
Updates

No need to include the logo for Drosval and Larkmoor containers.

Project Deadline Extended
Reason: would like to see more designs

Target Market(s)

purchasers of industrial companies

Industry/Entity Type

Business

Contact Information for Business Card

Korvelle Trade Center
Derek J. Foss
Please see attached old business card file for all the details.

Requirements
Must have
• All the texts in the attached card should be included (i.e. all the types of products)

Include the KORVELLE logo (update)
Include the DROSVAL logo (just copy)
Nice to have
• updated logo - still a bit recognizable but modern and have the letter "W".

```html
<!DOCTYPE html>
<html lang="en">
<head>
<meta charset="utf-8">
<title>Korvelle Trade Center – Business Card</title>
<link href="https://fonts.googleapis.com/css2?family=Arimo:wght@400;700&display=swap" rel="stylesheet">
<style>
  :root {
    --navy: #23246b;
    --ink: #1d1d1f;
    --grey: #3a3a3c;
    --rule: #5a5b8c;
    --paper: #ffffff;
    --backdrop: #c9cacd;
  }
  * { margin: 0; padding: 0; box-sizing: border-box; }
  html, body {
    width: 1200px; height: 900px; overflow: hidden;
    background: var(--backdrop);
    font-family: "Arimo", Arial, sans-serif;
  }
  .card {
    position: absolute; left: 150px; top: 193px;
    width: 900px; height: 514px;
    background: var(--paper);
    box-shadow: 0 6px 24px rgba(0,0,0,0.18);
    color: var(--ink);
  }
  .brand { position: absolute; left: 62px; top: 148px; display: flex; align-items: center; gap: 16px; }
  .brand-mark { width: 84px; height: 84px; background: var(--navy); }
  .brand-name {
    font-weight: 700; font-size: 33px; line-height: 0.95;
    color: var(--ink); letter-spacing: -0.5px; text-transform: uppercase;
  }
  .person { position: absolute; left: 520px; top: 62px; }
  .person-name { font-weight: 700; font-size: 31px; color: var(--navy); letter-spacing: 0.5px; }
  .person-cell { font-size: 17px; color: var(--grey); margin-top: 2px; }
  .label { color: var(--navy); }
  .rule { position: absolute; height: 1px; background: var(--rule); }
  .rule-top { left: 470px; top: 150px; width: 390px; }
  .rule-left { left: 62px; top: 345px; width: 420px; }
  .lines { position: absolute; font-size: 17px; line-height: 1.35; color: var(--grey); }
  .phones { left: 520px; top: 170px; }
  .office { left: 62px; top: 262px; }
  .office-name { font-weight: 700; font-size: 20px; color: var(--navy); }
  .products-main { left: 62px; top: 362px; }
  .products-side { left: 520px; top: 250px; }
  .accent-bar {
    position: absolute; left: 200px; right: 0; top: 462px; height: 26px;
    background: var(--navy);
  }
</style>
</head>
<body>
  <div class="card">
    <div class="brand">
      <div class="brand-mark"></div>
      <div class="brand-name">Korvelle<br>Trade Center</div>
    </div>

    <div class="person">
      <div class="person-name">DEREK J. FOSS</div>
      <div class="person-cell"><span class="label">Cell:</span> 0917.5530284</div>
    </div>

    <div class="rule rule-top"></div>

    <div class="lines phones">
      <div><span class="label">Tel:</span> 555.0142 / 555.0168 / 555.0193</div>
      <div><span class="label">Fax:</span> 555.0150</div>
    </div>

    <div class="lines products-side">
      <div>-Non-Asbestos Packing&amp; Gasket</div>
      <div>-Korvelle Maintenance Chemicals</div>
      <div>-Water Treatment Chemicals</div>
    </div>

    <div class="lines office">
      <div class="office-name">Korvelle Trade Center</div>
      <div>18 Calder Lane, Eastbank,</div>
      <div>Marlow Heights, Tervin City</div>
    </div>

    <div class="rule rule-left"></div>

    <div class="lines products-main">
      <div>-Rubber Roller &nbsp;-Mechanical Seal Products</div>
      <div>-Moulded Lining Products Polyuretane Roller</div>
      <div>-Moulded Lining Products Halvern Asbestos</div>
    </div>

    <div class="accent-bar"></div>
  </div>
</body>
</html>
```